Summit Vitality & Training Design

See photo attached
Obviously I want that second logo attached to it.
Summit Vitality & Training instead of the old one.
I had business cards already but I want to go back to a more professional look.
Open the some ideas but I would love around the same look that is shown on the photos. Easy money I would say for a designer

Target Market(s)

Fitness

Industry/Entity Type

Business

Contact Information for Business Card

Marcel Dufrenne
Director, Strength & Conditioning Head Coach
412 Garrick Street - Melbourne, Australia VIC 3000
0466293714
ABN 48261937408
mdufrenne@bravoriftfitness.com
www.bravoriftfitness.com
facebook.com/bravoriftfitness.com

Requirements
Must have
• Look Professional same or similar to uploaded photos.
• open to creativity
• black colour

```html
<!DOCTYPE html>
<html lang="en">
<head>
<meta charset="utf-8">
<title>Summit Vitality &amp; Training – Business Card</title>
<link rel="stylesheet" href="https://fonts.googleapis.com/css2?family=PT+Sans:wght@400;700&display=swap">
<style>
  :root {
    --stage: #3a3a3c;
    --card: #1d1a1c;
    --white: #f2f2f2;
    --grey: #c9c9c9;
    --red: #c8262c;
    --rule: #e6e6e6;
  }
  * { box-sizing: border-box; margin: 0; padding: 0; }
  html, body { width: 1200px; height: 900px; overflow: hidden; }
  body {
    background: var(--stage);
    font-family: "PT Sans", Arial, sans-serif;
    color: var(--white);
    display: flex;
    flex-direction: column;
    align-items: center;
    justify-content: center;
    gap: 50px;
  }
  .card {
    width: 620px;
    height: 355px;
    background: var(--card);
    border-radius: 22px;
    position: relative;
    box-shadow: 0 10px 30px rgba(0,0,0,.45);
  }

  /* front */
  .card--front {
    display: flex;
    align-items: center;
    justify-content: center;
  }
  .brand {
    display: flex;
    align-items: center;
    gap: 14px;
    font-weight: 700;
    color: var(--white);
    text-transform: uppercase;
    letter-spacing: 2px;
    line-height: 1.1;
  }
  .brand__mark {
    width: 22px; height: 22px;
    background: var(--red);
    flex: none;
  }
  .card--front .brand { font-size: 30px; }

  /* back */
  .card--back { display: flex; }
  .back__logo {
    width: 330px;
    display: flex;
    align-items: center;
    justify-content: center;
    padding: 0 26px;
  }
  .back__logo .brand { font-size: 24px; }
  .back__rule {
    width: 2px;
    background: var(--rule);
    margin: 40px 0;
  }
  .back__info {
    flex: 1;
    padding: 40px 22px 0 22px;
    font-size: 12.5px;
  }
  .info__brand {
    font-weight: 700;
    font-size: 17px;
    text-transform: uppercase;
    letter-spacing: 1px;
    line-height: 1.1;
    color: var(--white);
  }
  .person { margin-top: 14px; }
  .person__name {
    color: var(--red);
    font-weight: 700;
    text-transform: uppercase;
    font-size: 13px;
    letter-spacing: .5px;
  }
  .person__role { font-weight: 700; font-size: 11.5px; line-height: 1.3; }
  .person__abn { font-size: 9px; color: var(--grey); margin-left: 10px; }
  .contact { list-style: none; margin-top: 20px; }
  .contact__item {
    display: flex;
    align-items: flex-start;
    gap: 9px;
    line-height: 1.3;
    color: var(--grey);
    margin-bottom: 12px;
  }
  .contact__group .contact__item { margin-bottom: 3px; }
  .icon { width: 13px; height: 13px; flex: none; margin-top: 2px; fill: var(--red); }
  .icon--square { background: var(--red); border-radius: 2px; }
</style>
</head>
<body>

<section class="card card--front">
  <div class="brand"><span class="brand__mark"></span><span>Summit Vitality &amp; Training</span></div>
</section>

<section class="card card--back">
  <div class="back__logo">
    <div class="brand"><span class="brand__mark"></span><span>Summit Vitality &amp; Training</span></div>
  </div>
  <div class="back__rule"></div>
  <div class="back__info">
    <div class="info__brand">Summit Vitality &amp; Training</div>
    <div class="person">
      <div class="person__name">Marcel Dufrenne</div>
      <div class="person__role">Director</div>
      <div class="person__role">Strength &amp; Conditioning Head Coach</div>
      <div class="person__abn">ABN 48261937408</div>
    </div>
    <ul class="contact">
      <li class="contact__item">
        <svg class="icon" viewBox="0 0 16 16"><path d="M4 1l3 3-2 2c1 2 3 4 5 5l2-2 3 3-2 3C7 15 1 9 1 3z"/></svg>
        <span>0466 293 714</span>
      </li>
      <li class="contact__item">
        <svg class="icon" viewBox="0 0 16 16"><path d="M8 0a5.5 5.5 0 0 0-5.5 5.5C2.5 10 8 16 8 16s5.5-6 5.5-10.5A5.5 5.5 0 0 0 8 0zm0 8a2.5 2.5 0 1 1 0-5 2.5 2.5 0 0 1 0 5z"/></svg>
        <span>Level 2 &amp; 3, 412 Garrick Street<br>Melbourne, VIC 3000 Australia</span>
      </li>
      <li class="contact__group">
        <div class="contact__item">
          <svg class="icon" viewBox="0 0 16 16"><path d="M1 3h14v10H1z M1 3l7 6 7-6" fill="var(--red)" stroke="var(--card)" stroke-width="1.2"/></svg>
          <span>mdufrenne@bravoriftfitness.com</span>
        </div>
        <div class="contact__item">
          <span class="icon icon--square"></span>
          <span>/bravoriftfitness.com</span>
        </div>
        <div class="contact__item">
          <svg class="icon" viewBox="0 0 16 16"><circle cx="8" cy="8" r="7"/><path d="M1 8h14M8 1v14M3 4h10M3 12h10" stroke="var(--card)" stroke-width="1" fill="none"/><ellipse cx="8" cy="8" rx="3" ry="7" fill="none" stroke="var(--card)" stroke-width="1"/></svg>
          <span>www.bravoriftfitness.com</span>
        </div>
      </li>
    </ul>
  </div>
</section>

</body>
</html>
```